business card - for laser marking

I need design (curve) for my business card (make with laser) size 85mm x 55mm. How it look business card with laser marking see attached picture.

color:
Background: white
text and icons black

Please include: one side
1. damjan korošak - direktor
2. phone: +386(0)41 725 913
+386(0)597 162 84
3. info@vrezko.si
4. faecebook.com/Vrezko.Si
5. KL-DELAVNICA, Damjan Korošak s.p.
Brezova ulica 14, 1000 Ljubljana, SI
6. logo

Please include: second side
1. logo
2. www.vrezko.si
3. Lasersko graviranje
ovitki telefonov, ohišja telefonov / tablic, nakit, ure, alu vizitke, dog-tagi, kemični svinčniki, orodja, noži, vžigalniki

Industry/Entity Type

Business

Contact Information for Business Card

Please include: one side
+386(0)597 162 84
3. info@vrezko.si
6. logo

1. logo
2. www.vrezko.si
3. Lasersko graviranje

Colors
000000
ffffff

Requirements
Must have
• I need design (curve) for my business card (make with laser) size 85mm x 55mm. How it look business card with laser marking see attached picture.
• color:
• Background: white
• text and icons black
• Please include: one side
• 1. damjan korošak - direktor
• 2. phone: +386(0)41 725 913
• +386(0)597 162 84
• 3. info@vrezko.si
• 4. faecebook.com/Vrezko.Si
• 5. KL-DELAVNICA, Damjan Korošak s.p.
• Brezova ulica 14, 1000 Ljubljana, SI
• 6. logo
• Please include: second side
• 1. logo
• 2. www.vrezko.si
• 3. Lasersko graviranje
• ovitki telefonov, ohišja telefonov / tablic, nakit, ure, alu vizitke, dog-tagi, kemični svinčniki, orodja, noži, vžigalniki

```html
<!DOCTYPE html>
<html lang="sl">
<head>
<meta charset="utf-8">
<title>Vrezko – vizitke</title>
<link rel="stylesheet" href="https://fonts.googleapis.com/css2?family=Roboto:wght@400;700&display=swap">
<style>
  :root {
    --stage: #b2b2b2;
    --card-light: #f7f7f5;
    --card-dark: #3d3d3d;
    --ink-dark: #1e1e1e;
    --ink-light: #ffffff;
    --brand-accent: #d0164b;
  }
  html, body {
    margin: 0;
    padding: 0;
    width: 1200px;
    height: 791px;
    overflow: hidden;
    background: var(--stage);
    font-family: "Roboto", Arial, sans-serif;
  }
  .stage {
    position: relative;
    width: 1200px;
    height: 791px;
  }
  .card {
    position: absolute;
    top: 151px;
    width: 315px;
    height: 487px;
    text-align: center;
  }
  .card--front { left: 241px; color: var(--ink-dark); }
  .card--back  { left: 643px; color: var(--ink-light); }
  .card__shape {
    position: absolute;
    inset: 0;
    width: 315px;
    height: 487px;
  }
  .card--front .card__shape path { fill: var(--card-light); }
  .card--back  .card__shape path { fill: var(--card-dark); }
  .card__line {
    position: absolute;
    left: 0;
    right: 0;
    margin: 0;
    white-space: nowrap;
    line-height: 1;
  }
  .brand {
    top: 116px;
    font-size: 30px;
    font-weight: 700;
    letter-spacing: 1.5px;
  }
  .card--front .brand { color: var(--brand-accent); }
  .card--back  .brand { color: var(--ink-light); }
  .name  { top: 230px; font-size: 23px; font-weight: 700; }
  .role  { top: 257px; font-size: 14px; }
  .contact { font-size: 14px; }
  .phone-1  { top: 306px; }
  .phone-2  { top: 329px; }
  .email    { top: 359px; }
  .social   { top: 383px; }
  .company  { top: 413px; }
  .address  { top: 434px; }

  .services {
    position: absolute;
    left: 0;
    right: 0;
    top: 296px;
    margin: 0;
    padding: 0;
    list-style: none;
    font-size: 14px;
    line-height: 24px;
  }
  .website { top: 434px; font-size: 16px; font-weight: 700; }
</style>
</head>
<body>
<main class="stage">

  <section class="card card--front" aria-label="Vizitka, sprednja stran">
    <svg class="card__shape" viewBox="0 0 315 487" aria-hidden="true">
      <path d="M9,0 H306 Q315,0 315,9 Q300,243.5 315,478 Q315,487 306,487 H9 Q0,487 0,478 Q15,243.5 0,9 Q0,0 9,0 Z"/>
    </svg>
    <p class="card__line brand">VREZKO.si</p>
    <h1 class="card__line name">Damjan Korošak</h1>
    <p class="card__line role">Direktor</p>
    <p class="card__line contact phone-1">+386(0)41 725 913</p>
    <p class="card__line contact phone-2">+386(0)597 162 84</p>
    <p class="card__line contact email">info@vrezko.si</p>
    <p class="card__line contact social">facebook.com/Vrezko.Si</p>
    <p class="card__line contact company">KL-DELAVNICA, Damjan Korošak s.p.</p>
    <p class="card__line contact address">Brezova ulica 14, 1000 Ljubljana, SI</p>
  </section>

  <section class="card card--back" aria-label="Vizitka, zadnja stran">
    <svg class="card__shape" viewBox="0 0 315 487" aria-hidden="true">
      <path d="M9,0 H306 Q315,0 315,9 Q300,243.5 315,478 Q315,487 306,487 H9 Q0,487 0,478 Q15,243.5 0,9 Q0,0 9,0 Z"/>
    </svg>
    <p class="card__line brand">VREZKO.si</p>
    <h2 class="card__line name">Lasersko graviranje</h2>
    <ul class="services">
      <li>ovitki telefonov,</li>
      <li>ohišja telefonov / tablic,</li>
      <li>nakit, ure, alu vizitke,</li>
      <li>dog-tagi, kemični svinčniki,</li>
      <li>orodja, noži, vžigalniki</li>
    </ul>
    <p class="card__line website">www.vrezko.si</p>
  </section>

</main>
</body>
</html>
```